Website design for Kelvora Quad

Full Website Content Draft for: 'Kelvora Quad - A Financial Freedom Movement'

Header / Navigation
Logo (top left)
Navigation Links: Home | Our Story | Current State | Future State | How You Can Help | The Movement | Get Involved
CTA Button: Join the Movement
Homepage (Hero Section)

Headline:
Empowering Students. Transforming Futures.
Sub-Headline:
Financial literacy isn’t optional anymore — it’s essential.
Body (short):
Every year, millions of college students step into adulthood without the skills to manage money wisely. It’s time to change that.
Call-to-Action Button:
[Join the Movement]
Visual Suggestion:
Full-width image/video of diverse students on campus — upbeat, collaborative, inspiring.
Our Story

Section Header: Our Story
Body Copy:
For too long, financial literacy has been the missing piece of higher education. While students prepare academically for their futures, many graduate with financial stress, poor money habits, and debt that follows them for decades.
We believe knowledge is power — and financial literacy is freedom. With decades of combined experience in banking, leadership, and higher education, our team has seen the struggles firsthand. That’s why we’re committed to starting a movement that ensures every student leaves college not only with a degree, but with financial confidence.
The Current State

Section Header: The Current State
Infographic Copy / Stats:
70% of college students report finances as their #1 source of stress.*
43% of students don’t know their credit score.**
Student loan debt has surpassed $1.7 trillion.***
Subtext:
This is today’s reality. Students deserve better.
Footnotes (to place at bottom of page):
* Continental Scholar Wellness Society, Nationwide Pupil Vitality Survey, Spring 2022 Report.
** DORLANX & PMQ Pension Solutions, Coin Sense in the Dorms Study (2019).
*** Central Lending Board of Tamsworth, Consumer Credit Data (2024).
Visual Suggestion:
Infographic row with 3 icons (stress, credit, debt) and corresponding stats.
The Future State (Vision)

Section Header: The Future State (Vision)
Body Copy:
Imagine a campus where students graduate with more than a degree — they graduate with financial confidence.
They know how to budget, save, manage credit, and plan for their futures. They are free from fear, better equipped for life after graduation, and ready to thrive personally and professionally.
This is the future we are building together.
Visual Suggestion:
Smiling students celebrating graduation, overlay text “Confidence. Knowledge. Freedom.”
How You Can Help

Section Header: How You Can Help
Copy with Columns:
Universities
Partner with us to bring scalable, student-centered financial education to your campus.
Banks & Financial Institutions
Join us in shaping the next generation of financially confident customers while strengthening community impact.
Students & Parents
Be part of a movement that makes the college experience stronger, not harder.
Call-to-Action Button:
[Contact Us to Partner]
Visual Suggestion:
Three-column layout with icons (graduation cap for Universities, bank building for Banks, heart/people for Students & Parents).
The Movement

Section Header: The Movement
Body Copy:
This isn’t about one campus — it’s about a shift. A national movement to change the financial future for an entire generation. Together, we can rewrite the story.
We believe when students understand money, they reduce stress, gain freedom, and unlock their potential. That’s why this is more than a program — it’s a movement.
Visual Suggestion:
Map of the U.S. with “movement dots” spreading out, or collage of diverse students with bold words: Financial Literacy. Confidence. Future.
Get Involved (Contact Section)

Section Header: Get Involved
Body Copy:
Are you a university leader, bank executive, student, or parent who wants to be part of this movement? Let’s talk.
Contact Form Fields:
Name
Email
Role (University Faculty/Staff, Bank Partner, Student, Parent, Other)
Message
CTA Button: [Submit Interest]
Footer

Copy:
Join us in building the future of financial literacy.
Links: Privacy | Contact | Social Media (WorkLoop, Pixmora, etc.)
for my new Web Design Project will be added soon.

Target Market(s)

Partners: University Faculty and Bank Executives

Industry/Entity Type

Finance and Education

Coding

Coded - Design and coding required

Number of Pages Required

4 page

Font styles to use
Sans Serif

Colors

Designer to choose colors to be used in the design.

Requirements
Nice to have
• See description for details - This is a website to create a "movement" to help college and university students increase their financial literacy and reduce financial stress,

```html
<!DOCTYPE html>
<html lang="en">
<head>
<meta charset="utf-8">
<title>Kelvora Quad – A Financial Freedom Movement</title>
<link rel="stylesheet" href="https://fonts.googleapis.com/css2?family=Montserrat:wght@600;700;800;900&family=Inter:wght@400;500;600&display=swap">
<style>
:root{
  --blue:#1d8fe6;
  --blue-deep:#0a5fc2;
  --navy:#0a1530;
  --ink:#14161c;
  --muted:#5b6170;
  --ice:#e4f1fc;
  --white:#ffffff;
}
*{box-sizing:border-box;margin:0;padding:0}
html,body{width:1200px;height:2396px;overflow:hidden}
body{font-family:"Inter",Arial,sans-serif;color:var(--ink);background:var(--white);position:relative}
h1,h2,h3,.brand,.btn{font-family:"Montserrat",Arial,sans-serif}
.btn{display:inline-block;font-size:11px;font-weight:700;letter-spacing:.5px;padding:9px 18px;border-radius:4px;text-transform:uppercase;text-decoration:none}
.btn-outline{border:1.5px solid var(--ink);color:var(--ink)}
.btn-light{background:var(--white);color:var(--navy)}
.btn-dark{background:var(--navy);color:var(--white)}
.btn-blue{background:var(--blue);color:var(--white)}

/* hero */
.hero{position:absolute;left:0;top:0;width:1200px;height:590px;background:radial-gradient(ellipse at 50% 62%,#bfe6ff 0%,#2aa0ff 14%,#0b4fbf 38%,#071a4a 70%,#040a1f 100%);overflow:hidden}
.hero-curve{position:absolute;left:0;bottom:0;width:1200px;height:90px}
.nav{position:absolute;top:0;left:0;width:1200px;height:72px;display:flex;align-items:center;padding:0 60px;background:rgba(4,10,31,.55)}
.brand{display:flex;align-items:center;gap:8px;font-weight:800;font-size:20px;color:var(--white)}
.brand-mark{width:18px;height:18px;background:var(--blue);border-radius:3px}
.nav-links{display:flex;gap:26px;margin-left:auto;margin-right:26px;list-style:none}
.nav-links a{color:var(--white);font-size:11px;text-decoration:none;font-weight:500}
.hero-copy{position:absolute;top:285px;left:0;width:1200px;text-align:center;color:var(--white)}
.hero-copy h1{font-size:46px;font-weight:900;line-height:1.05;letter-spacing:.5px}
.hero-copy h1 .accent{color:#7cc7ff}
.hero-copy p{font-size:12px;max-width:560px;margin:14px auto 16px;line-height:1.5;color:#dbe9ff}

/* pillars */
.pillars{position:absolute;top:590px;left:240px;width:720px;display:flex}
.pillar{flex:1;height:170px;background:var(--ice);text-align:center;padding:26px 18px 0}
.pillar.is-featured{background:var(--blue);color:var(--white)}
.pillar svg{width:44px;height:36px}
.pillar h3{font-size:17px;font-weight:800;margin:10px 0 6px}
.pillar p{font-size:11px;color:var(--muted)}
.pillar.is-featured p{color:#dcefff}

/* story */
.story{position:absolute;top:800px;left:0;width:1200px;height:290px}
.section-title{font-size:40px;font-weight:900;line-height:1;text-transform:uppercase}
.section-title .accent{color:var(--blue)}
.story-text{position:absolute;left:220px;top:30px;width:330px}
.story-text p{font-size:11px;line-height:1.6;color:var(--muted);margin:16px 0}
.photo{background:linear-gradient(135deg,#caa98a,#7d8fa8 60%,#4b5a73)}
.story-collage{position:absolute;left:580px;top:10px;width:400px;height:270px}
.story-collage .p1{position:absolute;left:0;top:30px;width:190px;height:210px;border-radius:6px}
.story-collage .p2{position:absolute;left:200px;top:0;width:95px;height:120px;border-radius:6px}
.story-collage .p3{position:absolute;left:305px;top:0;width:95px;height:120px;border-radius:6px}
.story-collage .p4{position:absolute;left:200px;top:130px;width:95px;height:140px;border-radius:6px}
.story-collage .p5{position:absolute;left:305px;top:130px;width:95px;height:140px;border-radius:6px}
.story-collage .chip{position:absolute;left:170px;top:110px;width:52px;height:52px;border-radius:8px;background:var(--white);box-shadow:0 4px 14px rgba(0,0,0,.15);display:flex;align-items:center;justify-content:center;font:800 10px "Montserrat",Arial,sans-serif;color:var(--navy)}

/* current */
.current{position:absolute;top:1110px;left:0;width:1200px;height:360px}
.current-photo{position:absolute;left:0;top:0;width:600px;height:360px;background:linear-gradient(135deg,#9a8066,#5b6b55 50%,#2e3a44)}
.badges{position:absolute;left:150px;top:185px;display:flex;gap:18px}
.badge{width:82px;text-align:center;color:var(--white)}
.badge .ring{width:78px;height:78px;border-radius:50%;background:var(--blue);display:flex;flex-direction:column;align-items:center;justify-content:center;font:800 18px "Montserrat",Arial,sans-serif;border:3px solid rgba(255,255,255,.7)}
.badge .ring svg{width:22px;height:18px;margin-bottom:2px}
.badge small{display:block;font-size:9px;margin-top:6px;line-height:1.3}
.current-copy{position:absolute;left:660px;top:70px;width:480px}
.stats{display:flex;gap:28px;margin:26px 0 18px}
.stat b{display:block;font:800 28px "Montserrat",Arial,sans-serif;color:var(--blue)}
.stat span{font-size:10px;color:var(--muted);display:block;max-width:120px;line-height:1.3}
.current-copy .note{font-size:12px;margin-bottom:14px}

/* future */
.future{position:absolute;top:1480px;left:0;width:1200px;height:350px}
.future-copy{position:absolute;left:55px;top:60px;width:480px}
.future-copy p{font-size:11px;line-height:1.6;color:var(--muted);margin:14px 0}
.future-photo{position:absolute;left:600px;top:0;width:600px;height:345px;background:linear-gradient(135deg,#c49a72,#8a6a52 45%,#3c3f4d)}

/* cta */
.cta{position:absolute;top:1830px;left:0;width:1200px;height:260px;background:linear-gradient(180deg,#2a9cf0,#0f6fd6);text-align:center;color:var(--white);overflow:hidden}
.cta svg.wave{position:absolute;left:0;top:0;width:1200px;height:60px}
.cta h2{font-size:36px;font-weight:900;margin-top:95px}
.cta p{font-size:17px;margin:8px 0 16px}

/* footer */
.footer{position:absolute;top:2090px;left:0;width:1200px;height:306px;padding:0 60px}
.footer .brand{color:var(--navy);position:absolute;top:64px;left:200px;font-size:24px}
.footer-info{position:absolute;left:200px;top:112px;font-size:11px;color:var(--muted);line-height:1.9}
.footer-info a{color:var(--muted);text-decoration:none}
.footnotes{position:absolute;left:640px;top:50px;width:360px;height:150px;border:1.5px solid #c7ccd6;border-radius:8px;padding:16px 20px}
.footnotes h3{font-size:15px;font-weight:800;margin-bottom:8px}
.footnotes li{font-size:9.5px;color:var(--muted);line-height:1.5;list-style:none;margin-bottom:3px}
</style>
</head>
<body>

<header class="hero" role="img" aria-label="Blue light burst streaking toward the centre, symbolising momentum">
  <nav class="nav">
    <div class="brand"><span class="brand-mark"></span>Kelvora Quad</div>
    <ul class="nav-links">
      <li><a href="#">Home</a></li><li><a href="#">Our Story</a></li><li><a href="#">Current State</a></li>
      <li><a href="#">Future State</a></li><li><a href="#">How You Can Help</a></li><li><a href="#">The Movement</a></li><li><a href="#">Get Involved</a></li>
    </ul>
    <a class="btn btn-blue" href="#">Join the Movement</a>
  </nav>
  <div class="hero-copy">
    <h1>EMPOWERING <span class="accent">STUDENTS</span><br>TRANSFORMING FUTURES</h1>
    <p>Financial literacy isn’t optional anymore — it’s essential. Every year, millions of college students step into adulthood without the skills to manage money wisely. It’s time to change that.</p>
    <a class="btn btn-light" href="#">Learn More</a>
  </div>
  <svg class="hero-curve" viewBox="0 0 1200 90" preserveAspectRatio="none"><path d="M0 90 L0 70 Q600 -20 1200 70 L1200 90 Z" fill="#ffffff"/></svg>
</header>

<section class="pillars">
  <div class="pillar">
    <svg viewBox="0 0 44 36"><circle cx="14" cy="10" r="6" fill="#0a1530"/><circle cx="30" cy="10" r="6" fill="#0a1530"/><path d="M2 34c0-9 6-14 12-14s12 5 12 14zM18 34c0-9 6-14 12-14s12 5 12 14z" fill="#0a1530"/></svg>
    <h3>Student-Centered</h3><p>Built with higher-ed leaders in mind</p>
  </div>
  <div class="pillar is-featured">
    <svg viewBox="0 0 44 36"><rect x="6" y="18" width="7" height="16" fill="#fff"/><rect x="18" y="10" width="7" height="24" fill="#fff"/><rect x="30" y="3" width="7" height="31" fill="#fff"/></svg>
    <h3>Evidence-Led</h3><p>Grounded in research and outcomes</p>
  </div>
  <div class="pillar">
    <svg viewBox="0 0 44 36"><circle cx="11" cy="9" r="5" fill="#0a1530"/><circle cx="33" cy="9" r="5" fill="#0a1530"/><path d="M2 30c0-8 4-13 9-13s9 5 9 13zM24 30c0-8 4-13 9-13s9 5 9 13z" fill="#0a1530"/><rect x="16" y="22" width="12" height="4" rx="2" fill="#1d8fe6"/></svg>
    <h3>Partnership-Ready</h3><p>Designed for universities &amp; banks</p>
  </div>
</section>

<section class="story">
  <div class="story-text">
    <h2 class="section-title">Our Story</h2>
    <p>For too long, financial literacy has been the missing piece of higher education. While students prepare academically for their futures, many graduate with financial stress, poor money habits, and debt that follows them for decades. We believe knowledge is power — and financial literacy is freedom.</p>
    <a class="btn btn-outline" href="#">Learn More</a>
  </div>
  <div class="story-collage">
    <div class="photo p1" role="img" aria-label="Smiling student on campus"></div>
    <div class="photo p2" role="img" aria-label="Students studying together"></div>
    <div class="photo p3" role="img" aria-label="Student group outdoors"></div>
    <div class="photo p4" role="img" aria-label="Students collaborating at a table"></div>
    <div class="photo p5" role="img" aria-label="Students walking on campus"></div>
    <div class="chip">KQ</div>
  </div>
</section>

<section class="current">
  <div class="current-photo" role="img" aria-label="Worried students looking at phones and bills"></div>
  <div class="badges">
    <div class="badge"><div class="ring"><svg viewBox="0 0 22 18"><circle cx="11" cy="9" r="7" fill="none" stroke="#fff" stroke-width="2"/><path d="M7 12q4-4 8 0" stroke="#fff" stroke-width="2" fill="none"/></svg>70%</div><small>report finances as top stress</small></div>
    <div class="badge"><div class="ring"><svg viewBox="0 0 22 18"><rect x="1" y="3" width="20" height="13" rx="2" fill="none" stroke="#fff" stroke-width="2"/><rect x="1" y="6" width="20" height="3" fill="#fff"/></svg>43%</div><small>don’t know their credit score</small></div>
    <div class="badge"><div class="ring"><svg viewBox="0 0 22 18"><path d="M11 1 L21 6 L11 11 L1 6 Z" fill="#fff"/><path d="M5 9v5q6 4 12 0V9" fill="none" stroke="#fff" stroke-width="2"/></svg>$1.7T</div><small>in student loan debt</small></div>
  </div>
  <div class="current-copy">
    <h2 class="section-title">The Current State</h2>
    <div class="stats">
      <div class="stat"><b>70% of college students</b><span>Report finances as their #1 source of stress.*</span></div>
      <div class="stat"><b>43%</b><span>of students don’t know their credit score.**</span></div>
      <div class="stat"><b>$1.7 trillion</b><span>Student loan debt has surpassed $1.7 trillion.***</span></div>
    </div>
    <p class="note">This is today’s reality. Students deserve better.</p>
    <a class="btn btn-outline" href="#">See the Data</a>
  </div>
</section>

<section class="future">
  <div class="future-copy">
    <h2 class="section-title">The Future State<br><span class="accent">(Vision)</span></h2>
    <p>Imagine a campus where students graduate with more than a degree — they graduate with financial confidence.</p>
    <p>They know how to budget, save, manage credit, and plan for their futures. They are free from fear, better equipped for life after graduation, and ready to thrive personally and professionally.</p>
    <a class="btn btn-outline" href="#">Explore the Vision</a>
  </div>
  <div class="future-photo" role="img" aria-label="Students gathered around a table, confident and engaged"></div>
</section>

<section class="cta">
  <svg class="wave" viewBox="0 0 1200 60" preserveAspectRatio="none"><path d="M0 0 H1200 V10 Q600 70 0 10 Z" fill="#ffffff"/></svg>
  <h2>READY TO HELP BUILD THE MOVEMENT?</h2>
  <p>Universities, banks, students, and parents all have a role to play</p>
  <a class="btn btn-dark" href="#">Get Involved</a>
</section>

<footer class="footer">
  <div class="brand"><span class="brand-mark"></span>Kelvora Quad</div>
  <div class="footer-info">
    <p>Join us in building the future of financial literacy.</p>
    <p><a href="#">Privacy</a> | <a href="#">Contact</a> | <a href="#">WorkLoop</a> | <a href="#">Pixmora</a></p>
    <p>© 2025 Kelvora Quad</p>
  </div>
  <aside class="footnotes">
    <h3>Footnotes</h3>
    <ul>
      <li>* Continental Scholar Wellness Society, Nationwide Pupil Vitality Survey, Spring 2022 Report.</li>
      <li>** DORLANX &amp; PMQ Pension Solutions, Coin Sense in the Dorms Study (2019).</li>
      <li>*** Central Lending Board of Tamsworth, Consumer Credit Data (2024).</li>
    </ul>
  </aside>
</footer>

</body>
</html>
```